I am looking for a web design that includes space for a blog, archive and an
“ about me” section. It should be capable of being updated in the future should I decide to build the site. I like edgy, creative, friendly and inviting to go with my logo style.
The Plate Ledger is an approach to breaking down and rebuilding or just tweaking what needs to be done to reach nutritional fitness. That is the actual workout part....journaling through something I call reflective nutrition. By doing this one can actually see what they are doing well and where they may need to improve. It involves goal setting and analyzing one's relationship with food. the workout is more mental in this approach. Physical activity is definitely a part of a strong nutritional foundation, but here I am focusing on the work that goes into creating a positive nutritionally fit person.

1. Blog Section: this will be the foundation of the website. I will write weekly blogs explaining and encouraging readers to use reflective nutrition approach to discover and explore their relationship with food and create healthy nutritional habits, breaking those that have been detrimental thus far. Journaling and realistic goal setting is the key to this approach.

2. Archive: this is the section to store old blogs by date with ability to retrieve and read again. Readers should gave access to this section.

3. About Me: I am a clinical nutritionist with a Bachelors of Science and Masters of Science in Nutrition. I have over 30 years experience working with both inpatient and outpatient populations covering a myriad of conditions requiring nutritional intervention. I am passionate about my field and my goal is to help others achieve their optimal nutritional health. I will share my personal struggle with attaining nutritional fitness. I have the
unique perspective of being both a nutrition professional and patient.
Please note that my blog name is not the name under which I am registered with the Board For Dietary Credentialing (BDC).Contact me privately if you require more information.
Thank you for stopping by and I hope you will come back.
Peace,
M. Harlow
4. Contact Me: This section will only contain my email address for comments and suggestions Theplateledger@mailnest.example
Updates

Hey guys! I am very new to this process and I apologize for not having much detail. I think I added more that may give you a clearer understanding of my project. I know I said that I didn't plan on using illustrations but I am getting a better picture of what you do. Please use all your creative tools and talents and imaginations! But read my description of what the actual nutrition workout is. It is more of a mental not physical workout. I will respond to your questions and suggestions. I welcome them. Have fun with this!!! I look forward to seeing your work. . Peace, Mira

Target Market(s)

Anyone interested in a realistic approach to reaching nutrition goals.

Industry/Entity Type

Nutrition

Coding

Coded - Design and coding required

Number of Pages Required

3 page

Colors
fbee3d
ffc214

Requirements
Must have
• An automatic sign-off signature at the end of each blog, preferably in the same font as my logo name. Signature will read:
Peace,
B.
My blog name is M, Harlow
Complementary color scheme to the logo but not white, if at all possible. I don't plan on using illustrations so I am relying on the web design to draw people in. It cannot be dull or bland but still professional.
It must be inviting and personable, not intimidating
I may want to update and add on later. Site should be capable of doing
that....should be buildable.
I love the font that was used in the name of my logo and would like to stay consistant with that, if possible.
Nice to have
• A way to monitor people who visit and return.
Maybe a counter to see how many people have visited
Would it be possible to prominently display my logo on the first page with my contact information and have that open directly to my blog page? Also, would the block page have to be a white background? I prefer it to be a color if that is complementary to the logo olor scheme
Should not have
• Please no illustrations of a gym.
This isn’t a blog about physical fitness. It is a blog requiring people to think about what they consume on a daily basis, breaking bad eating habits and creating positive, healthy ones.
I tried to get pictures and illustrations to use but due to licensure restrictions, I was unable at this time. Although your designs are brilliant, I may not be able to supply appropriate illustrations to do your designs justice.

```html
<!DOCTYPE html>
<html lang="en">
<head>
<meta charset="utf-8">
<title>Mira Nutrition</title>
<link rel="stylesheet" href="https://fonts.googleapis.com/css2?family=Arimo:wght@400;700&family=Lato:wght@400;700&family=Libre+Baskerville&display=swap">
<style>
:root{
  --gold:#cbb30c;
  --black:#000;
  --ink:#0c0c0c;
  --white:#fff;
  --muted:#e6e6e6;
}
*{margin:0;padding:0;box-sizing:border-box}
html,body{width:1200px;height:2329px;overflow:hidden;background:var(--black);color:var(--white)}
body{position:relative;font-family:"Lato",sans-serif}
.abs{position:absolute}
.sans{font-family:"Arimo",sans-serif}
.btn{position:absolute;background:var(--gold);color:var(--white);font-family:"Arimo",sans-serif;font-weight:700;font-size:15px;display:flex;align-items:center;justify-content:center}
.icon-dot{display:inline-flex;width:28px;height:28px;border-radius:50%;align-items:center;justify-content:center}

/* top bar */
.topbar{left:0;top:0;width:1200px;height:45px;background:var(--black);font-family:"Arimo",sans-serif;font-size:15px}
.topbar .item{position:absolute;top:8px;display:flex;align-items:center;gap:10px}
.topbar .icon-dot{background:var(--white)}
.follow{position:absolute;right:86px;top:13px;display:flex;align-items:center;gap:10px}
.follow span.sq{width:11px;height:11px;background:var(--white);display:inline-block}

/* hero */
.hero{left:0;top:45px;width:1200px;height:575px;background:radial-gradient(ellipse at 58% 40%,#5a4a44 0%,#2a2528 35%,#141218 70%,#0b0a0f 100%)}
.brand{left:86px;top:70px;width:130px;color:var(--gold);font-family:"Arimo",sans-serif;font-weight:700;font-size:22px;line-height:1.15;display:flex;align-items:center;gap:8px}
.brand .mark{width:14px;height:14px;border-radius:50%;background:var(--gold);flex:none}
.nav{left:262px;top:86px;display:flex;gap:0;font-family:"Arimo",sans-serif;font-size:16.5px}
.nav a{color:var(--white);text-decoration:none;position:absolute;white-space:nowrap}
.hero-title{left:83px;top:236px;font-family:"Arimo",sans-serif;font-weight:700;font-size:48px}
.hero-text{left:85px;top:298px;width:460px;font-size:15px;line-height:26px}
.dots{left:617px;top:551px;display:flex;gap:5px}
.dots i{width:13px;height:13px;border-radius:50%;background:var(--white);display:block}
.dots i:first-child{background:var(--gold)}

/* about */
.about-photo{left:86px;top:706px;width:449px;height:394px;background:linear-gradient(135deg,#e8c43a 0%,#e9a889 35%,#dfe3e4 55%,#6aa14a 80%,#d9572a 100%)}
.about-box{left:487px;top:748px;width:628px;height:312px;background:var(--black)}
.h2{font-family:"Arimo",sans-serif;font-weight:700;font-size:39px;position:absolute}
.rule{position:absolute;height:2px;width:60px;background:var(--gold)}
.about-text{left:531px;top:850px;width:555px;font-size:15.5px;line-height:26px}

/* blog */
.blog{left:0;top:1188px;width:1200px;height:717px;background:radial-gradient(ellipse at 50% 30%,#262626 0%,#151515 60%,#0e0e0e 100%)}
.card{position:absolute;border:1px solid var(--gold);background:var(--black)}
.card .thumb{position:absolute}
.card h3{position:absolute;font-family:"Arimo",sans-serif;font-weight:700;font-size:15.5px}
.date{position:absolute;display:flex;align-items:center;gap:8px;color:var(--gold);font-family:"Arimo",sans-serif;font-size:15px}
.card p{position:absolute;font-family:"Arimo",sans-serif;font-size:15px;line-height:26px}

/* footer */
.footer{left:0;top:1905px;width:1200px;height:424px;background:var(--black)}
.foot-brand{left:84px;top:1943px;font-family:"Libre Baskerville",serif;font-size:26px}
.foot-h{position:absolute;top:1951px;font-family:"Arimo",sans-serif;font-size:17.5px}
.list{position:absolute;list-style:none;font-size:16px}
.list li{height:37.5px;display:flex;align-items:center;gap:10px}
.chev{color:var(--gold);font-size:12px}
.sqi{width:11px;height:11px;background:var(--gold);display:inline-block;margin-right:4px}
.contact{position:absolute;left:843px;font-size:16px;display:flex;align-items:flex-start;gap:12px}
.contact .icon-dot{background:var(--gold);width:30px;height:30px;flex:none}
.divider{left:84px;top:2234px;width:1028px;height:1px;background:#555}
.copy{left:0;top:2268px;width:1200px;text-align:center;font-size:16px}
</style>
</head>
<body>

<!-- top bar -->
<div class="abs topbar">
  <div class="item" style="left:85px">
    <span class="icon-dot"><svg width="14" height="14" viewBox="0 0 24 24"><path fill="#cbb30c" d="M6.6 10.8a15 15 0 006.6 6.6l2.2-2.2c.3-.3.7-.4 1-.2 1.1.4 2.3.6 3.6.6.6 0 1 .4 1 1V20c0 .6-.4 1-1 1A17 17 0 013 4c0-.6.4-1 1-1h3.5c.6 0 1 .4 1 1 0 1.3.2 2.5.6 3.6.1.3 0 .7-.2 1z"/></svg></span>
    555-0142-318
  </div>
  <div class="item" style="left:248px">
    <span class="icon-dot"><svg width="14" height="12" viewBox="0 0 24 18"><rect x="1" y="1" width="22" height="16" rx="2" fill="none" stroke="#cbb30c" stroke-width="2"/><path d="M2 2l10 8 10-8" fill="none" stroke="#cbb30c" stroke-width="2"/></svg></span>
    Theplateledger@mailnest.example
  </div>
  <div class="follow">Follows Us: <span class="sq"></span><span class="sq"></span><span class="sq"></span><span class="sq"></span></div>
</div>

<!-- hero -->
<section class="abs hero" role="img" aria-label="Athlete seated on a bench in a dimly lit training room"></section>
<div class="abs brand"><span class="mark"></span>The Plate Ledger</div>
<nav class="abs nav">
  <a style="left:0">Home</a>
  <a style="left:107px">About Me</a>
  <a style="left:240px">Services</a>
  <a style="left:367px">Blog</a>
  <a style="left:462px">Testimonials</a>
  <a style="left:614px">Contact us</a>
</nav>
<svg class="abs" style="left:1037px;top:87px" width="20" height="22" viewBox="0 0 20 22"><circle cx="10" cy="6" r="5" fill="none" stroke="#fff" stroke-width="1.6"/><path d="M1 21c0-5 4-8 9-8s9 3 9 8z" fill="none" stroke="#fff" stroke-width="1.6"/></svg>
<svg class="abs" style="left:1091px;top:87px" width="23" height="23" viewBox="0 0 23 23"><circle cx="9.5" cy="9.5" r="8" fill="none" stroke="#fff" stroke-width="1.6"/><path d="M15.5 15.5l6 6" stroke="#fff" stroke-width="1.6"/></svg>
<h1 class="abs hero-title">Mira Nutrition</h1>
<p class="abs hero-text">Lorem ipsum dolor sit amet, consectetur adipiscing elit, eiusmod tempor incididunt ut labore et dolore magna aliqua.</p>
<div class="btn" style="left:85px;top:375px;width:101px;height:33px">Get started</div>
<div class="abs dots"><i></i><i></i><i></i></div>

<!-- about -->
<div class="abs about-photo" role="img" aria-label="Table spread of fruit, vegetables, salmon, oil and grains"></div>
<div class="abs about-box"></div>
<h2 class="h2" style="left:531px;top:765px">About Me</h2>
<div class="rule" style="left:531px;top:830px"></div>
<p class="abs about-text">&nbsp;I am a clinical nutritionist with a Bachelors of Science and Masters of Science in Nutrition. I have over 30 years experience working with both inpatient and outpatient populations covering a myriad of conditions requiring nutritional intervention. I am passionate about my field and my goal is to help others achieve their optimal nutritional health.</p>
<div class="btn" style="left:531px;top:999px;width:107px;height:34px">Learn More</div>

<!-- blog & archive -->
<section class="abs blog"></section>
<h2 class="h2" style="left:88px;top:1256px">Our Blog</h2>
<div class="rule" style="left:90px;top:1320px;width:85px"></div>
<h2 class="h2" style="left:705px;top:1256px">Archive</h2>
<div class="rule" style="left:706px;top:1320px;width:85px"></div>

<article class="card" style="left:89px;top:1367px;width:577px;height:221px">
  <div class="thumb" role="img" aria-label="Bowl of ground flour beside baked rolls" style="left:14px;top:8px;width:237px;height:205px;background:linear-gradient(135deg,#6b4a2c 0%,#c9ac74 45%,#e4cf9c 70%,#8b6a3f 100%)"></div>
  <h3 style="left:293px;top:19px">Lorem ipsum dolor sit ame</h3>
  <div class="date" style="left:293px;top:51px"><svg width="16" height="16" viewBox="0 0 16 16"><rect x="1" y="3" width="14" height="12" fill="none" stroke="#cbb30c" stroke-width="1.3"/><path d="M1 6h14M4 1v4M12 1v4" stroke="#cbb30c" stroke-width="1.3"/></svg>Feb 12,2021</div>
  <p style="left:293px;top:78px;width:260px">Lorem ipsum dolor sit amet, consectetur adipiscing elit, sed do eiusmod tempor incididunt ut</p>
  <div class="btn" style="left:293px;top:164px;width:110px;height:33px">Read More</div>
</article>

<article class="card" style="left:89px;top:1613px;width:577px;height:221px">
  <div class="thumb" role="img" aria-label="Plate of fresh salad with dumbbells and a tape measure" style="left:14px;top:8px;width:237px;height:205px;background:linear-gradient(135deg,#6a4a32 0%,#4fb7d6 30%,#e9e4dc 55%,#3f8a3a 75%,#6a4a32 100%)"></div>
  <h3 style="left:293px;top:19px">Lorem ipsum dolor sit ame</h3>
  <div class="date" style="left:293px;top:51px"><svg width="16" height="16" viewBox="0 0 16 16"><rect x="1" y="3" width="14" height="12" fill="none" stroke="#cbb30c" stroke-width="1.3"/><path d="M1 6h14M4 1v4M12 1v4" stroke="#cbb30c" stroke-width="1.3"/></svg>Feb 8,2021</div>
  <p style="left:293px;top:78px;width:260px">Lorem ipsum dolor sit amet, consectetur adipiscing elit, sed do eiusmod tempor incididunt ut</p>
  <div class="btn" style="left:293px;top:164px;width:110px;height:33px">Read More</div>
</article>

<article class="card" style="left:705px;top:1367px;width:411px;height:467px">
  <div class="thumb" role="img" aria-label="Water bottle, dumbbells, nuts and fresh fruit on a wooden table" style="left:10px;top:20px;width:390px;height:169px;background:linear-gradient(90deg,#7a5a3c 0%,#5ec3dc 25%,#a2633c 50%,#c8262f 65%,#f0d048 85%,#7a5a3c 100%)"></div>
  <h3 style="left:13px;top:221px">Lorem ipsum dolor sit amet, consectetur</h3>
  <div class="date" style="left:14px;top:265px"><svg width="19" height="19" viewBox="0 0 16 16"><rect x="1" y="3" width="14" height="12" fill="none" stroke="#cbb30c" stroke-width="1.3"/><path d="M1 6h14M4 1v4M12 1v4" stroke="#cbb30c" stroke-width="1.3"/></svg>Feb 10,2019</div>
  <p style="left:14px;top:310px;width:385px">Lorem ipsum dolor sit amet, consectetur adipiscing elit, sed do eiusmod tempor incididunt ut labore et dolore magna aliqua.</p>
  <div class="btn" style="left:14px;top:404px;width:114px;height:41px">Learn More</div>
</article>

<!-- footer -->
<footer class="abs footer"></footer>
<div class="abs foot-brand">Mira Nutrition</div>
<div class="foot-h" style="left:84px;top:2010px">Follows Us:</div>
<ul class="list" style="left:84px;top:2049px">
  <li><span class="sqi"></span>Friendbook</li>
  <li><span class="sqi"></span>Chirper</li>
  <li><span class="sqi"></span>Snapgram</li>
  <li><span class="sqi"></span>Linkwork</li>
</ul>

<div class="foot-h" style="left:386px">Quicklinks</div>
<ul class="list" style="left:386px;top:1983px">
  <li><span class="chev">&gt;</span>Home</li>
  <li><span class="chev">&gt;</span>About Me</li>
  <li><span class="chev">&gt;</span>Services</li>
  <li><span class="chev">&gt;</span>Our Blog</li>
  <li><span class="chev">&gt;</span>Testimonials</li>
  <li><span class="chev">&gt;</span>Contact Us</li>
</ul>

<div class="foot-h" style="left:624px">Otherlinks</div>
<ul class="list" style="left:624px;top:1983px">
  <li><span class="chev">&gt;</span>Team</li>
  <li><span class="chev">&gt;</span>Support</li>
  <li><span class="chev">&gt;</span>Services</li>
  <li><span class="chev">&gt;</span>Privacy Policy</li>
  <li><span class="chev">&gt;</span>FAQ</li>
</ul>

<div class="foot-h" style="left:843px">Contact Us</div>
<div class="contact" style="top:1992px">
  <span class="icon-dot"><svg width="14" height="14" viewBox="0 0 24 24"><path fill="#fff" d="M6.6 10.8a15 15 0 006.6 6.6l2.2-2.2c.3-.3.7-.4 1-.2 1.1.4 2.3.6 3.6.6.6 0 1 .4 1 1V20c0 .6-.4 1-1 1A17 17 0 013 4c0-.6.4-1 1-1h3.5c.6 0 1 .4 1 1 0 1.3.2 2.5.6 3.6.1.3 0 .7-.2 1z"/></svg></span>
  <span style="padding-top:4px">555-0142-318</span>
</div>
<div class="contact" style="top:2044px">
  <span class="icon-dot"><svg width="14" height="12" viewBox="0 0 24 18"><rect x="1" y="1" width="22" height="16" rx="2" fill="none" stroke="#fff" stroke-width="2"/><path d="M2 2l10 8 10-8" fill="none" stroke="#fff" stroke-width="2"/></svg></span>
  <span style="padding-top:4px;font-size:15.5px">Theplateledger@mailnest.example</span>
</div>
<div class="contact" style="top:2096px">
  <span class="icon-dot" style="margin-top:10px"><svg width="12" height="16" viewBox="0 0 12 16"><path d="M6 0a6 6 0 016 6c0 4-6 10-6 10S0 10 0 6a6 6 0 016-6z" fill="#fff"/><circle cx="6" cy="6" r="2" fill="#cbb30c"/></svg></span>
  <span style="line-height:26px">231, Sed ut perspiciatis unde<br>&nbsp;iste natus error sit vo</span>
</div>

<div class="abs divider"></div>
<div class="abs copy">&copy;Copyrights 2021&nbsp; Mira Nutrition &nbsp;|&nbsp;&nbsp; All Rights Reserved &nbsp;|</div>

</body>
</html>
```